magcian / mentalist needs flyer desined to send potentisl clients

I need a design that's contemporary, sharp, fun, and professional that will get the attention of whoever receives the flyer very quickly. This is for a tri-fold flyer design.

I've been performing magic for over 40 years. I've performed close-up,
parlor, and stage shows. I've been an Master of Ceremonies, Key Note
Speaker (using magic during presentations to help build on a point or
topic, while keeping the audience entertained and educated on the topic or
topics the client has asked me to focus). I've worked trade shows and
sales training incorporating magic as well. I did private shows in Las
Vegas and L.A. back in the late 90's as well.

I do have website / walterbrisbymagic.example for your to check out.

Target Market(s)

The target audience is corporation Event Planners, Marketing and Sales
managers, casino & hotel entertainment directors, as well as private
businesses looking for unique entertainment options.

Industry/Entity Type

Entertainment Industry

Logo Text

Here are a couple of ideas: your mind is my playground, neural entertainer, professor of mysteries, master of your mind

Requirements
Must have
• I like the black and white look (I think it looks nice, but open to other
• ideas and creativity. Being I'm a magician and mentalist, I'd like for
• both venues to be conveyed somehow. My magic is clean and corporate and family friendly.
Nice to have
• I do have website / walterbrisbymagic.example for your to check out.
• My current business card is attached for review. I'll also attach photos
• I'd like to share, but was unable when I last attempted do sign up. Some
• of the files were too big and I'm not savvy enough to make them smaller,
• but think there might be some potential with a couple.
Should not have
• cartoons or cartoonish graphics. no rabbits, doves, magicians, wands, or top hats.

```html
<!DOCTYPE html>
<html lang="en">
<head>
<meta charset="utf-8">
<title>Walter Brisby – Tri-fold Brochure</title>
<link href="https://fonts.googleapis.com/css2?family=Cinzel:wght@400;700&family=Lato:ital,wght@0,400;0,700;1,700&family=Oswald:wght@500&family=Tinos:wght@700&family=Roboto+Condensed:wght@700&display=swap" rel="stylesheet">
<style>
:root{
  --backdrop:#aa9b8a;
  --red:#d3141c;
  --red-deep:#6e0508;
  --red-bright:#ec1c24;
  --black:#0b0b0b;
  --ink:#111;
  --white:#fff;
  --grey:#3a3a3a;
  --silver:#cfcfcf;
}
*{box-sizing:border-box;margin:0;padding:0}
html,body{width:907px;height:1200px;overflow:hidden}
body{background:var(--backdrop);position:relative;font-family:'Lato',sans-serif;color:var(--white)}
.sheet{position:absolute;left:80px;width:742px;height:528px;overflow:hidden;background:var(--black)}
.sheet--outside{top:52px}
.sheet--inside{top:612px}
.panel{position:absolute;top:0;height:100%;overflow:hidden}
.panel--a{left:0;width:252px}
.panel--b{left:252px;width:244px}
.panel--c{left:496px;width:246px}
.fill-red{background:linear-gradient(180deg,var(--black) 0%,var(--red-deep) 35%,var(--red) 70%,var(--red-deep) 100%)}
.fill-red-soft{background:linear-gradient(180deg,var(--red-deep) 0%,var(--red) 40%,#b50d14 75%,var(--red-deep) 100%)}
.photo{position:absolute}
.deco{position:absolute;left:0;top:0;pointer-events:none}
.body-copy{position:absolute;font-size:8.6px;line-height:1.3;text-align:justify;color:var(--white)}
.body-copy p+p{margin-top:6px}
.body-copy--tight{font-size:8.1px;line-height:1.26}
.heading-light{font-family:'Cinzel',serif;font-weight:400;color:var(--white);text-align:center;position:absolute;width:100%}
.heading-dark{font-family:'Cinzel',serif;font-weight:700;color:var(--ink);text-align:center;position:absolute;width:100%}
.brand-name{position:absolute;width:100%;text-align:center;font-family:'Lato',sans-serif;font-weight:400;color:var(--white)}
.brand-roles{position:absolute;width:100%;text-align:center;font-size:6.5px;letter-spacing:.3px;color:var(--white)}
.brand-roles .accent{color:var(--red-bright)}
.studio{position:absolute;width:100%;text-align:center;font-family:'Tinos',serif;font-weight:700}
.phone{position:absolute;width:100%;text-align:center;font-family:'Oswald',sans-serif;font-weight:500;font-size:27px;letter-spacing:1px}
.contact-list{position:absolute;left:22px;list-style:none;font-size:10.5px}
.contact-list li{display:flex;align-items:center;gap:8px;height:21px}
.contact-list svg{flex:none}
.contact-list .square{width:9px;height:9px;background:var(--red);flex:none}
.pill{position:absolute;left:50%;transform:translateX(-50%);border:2px solid var(--silver);border-radius:6px;text-align:center;white-space:nowrap}
.pill--tagline{background:var(--black);font-family:'Tinos',serif;font-weight:700;font-size:10.5px;letter-spacing:.6px;padding:3px 10px}
.pill--keynote{background:var(--black);font-family:'Roboto Condensed',sans-serif;font-weight:700;font-size:13px;padding:2px 14px;border-radius:9px}
.pill--services{background:var(--red);font-family:'Roboto Condensed',sans-serif;font-weight:700;font-size:20px;padding:0 26px;border-radius:9px;letter-spacing:.5px}
.site-line{position:absolute;width:100%;text-align:center;font-family:'Tinos',serif;font-weight:700;font-size:9px;letter-spacing:2px;color:var(--white)}
.service-list{position:absolute;list-style:none;font-size:9.5px;font-weight:700;font-style:italic}
.service-list li{height:18px;display:flex;align-items:center;gap:6px}
.service-list li::before{content:"";width:5px;height:5px;border-radius:50%;background:var(--red-bright)}
.eyebrow{position:absolute;width:100%;text-align:center;font-family:'Cinzel',serif;font-weight:700;font-size:11.5px;color:var(--white)}
.headline{position:absolute;width:100%;text-align:center;font-family:'Cinzel',serif;font-weight:400;color:var(--black)}
</style>
</head>
<body>

<section class="sheet sheet--outside">

  <div class="panel panel--a fill-red">
    <div class="photo" role="img" aria-label="Photo of the magician performing a mentalism routine on stage with a blindfolded participant and a volunteer holding a framed picture"
      style="left:0;top:0;width:252px;height:260px;background:linear-gradient(160deg,#1a1f3a,#3b2a40 55%,#5a1d22);clip-path:polygon(0 62px,120px 30px,252px 58px,252px 220px,120px 250px,0 222px)"></div>
    <svg class="deco" width="252" height="270" viewBox="0 0 252 270" aria-hidden="true">
      <polyline points="0,58 120,26 252,54" fill="none" stroke="var(--white)" stroke-width="2"/>
      <polyline points="0,50 120,18 252,46" fill="none" stroke="var(--red-bright)" stroke-width="8"/>
      <polyline points="0,226 120,254 252,224" fill="none" stroke="var(--silver)" stroke-width="3"/>
      <polyline points="0,234 120,262 252,232" fill="none" stroke="var(--black)" stroke-width="6"/>
    </svg>
    <h2 class="heading-light" style="top:270px;font-size:24px">ABOUT</h2>
    <h2 class="heading-dark" style="top:296px;font-size:33px">WALTER</h2>
    <div class="body-copy" style="left:20px;top:341px;width:214px">
      <p><span style="font-family:'Cinzel',serif;font-size:13px">A</span> magician as an entertainer, or speaker at your events will provide a different level of experience to your guests or clients, elevating your events!</p>
      <p>I’m a professional entertainer. I’ve performed all over the country for major corporations which means you’re getting tried and true, first-rate entertainment. Doing business with me is easy. I make sure you’re comfortable with every step in the process of dealing with me. From booking to follow-up you’ll be happy. I arrive early to your event, start on time, and deliver a great performance. You might have a lot on your mind on the day of your event, but worrying about the entertainment won’t be one of them.</p>
    </div>
  </div>

  <div class="panel panel--b" style="background:linear-gradient(180deg,#222 0%,#141414 50%,#2a2a2a 100%)">
    <div class="photo" role="img" aria-label="Ornate dark engraved illustration framing the top of the panel"
      style="left:0;top:0;width:244px;height:270px;background:radial-gradient(ellipse at 50% 40%,#6a6a6a 0%,#2c2c2c 55%,#151515 100%)"></div>
    <div class="photo" role="img" aria-label="Faint dark photo of hands performing a card trick"
      style="left:0;top:420px;width:244px;height:108px;background:linear-gradient(180deg,rgba(40,40,40,0),#4a4a4a 60%,#2a2a2a)"></div>
    <div class="brand-name" style="top:268px;font-size:15px">walter brisby</div>
    <div class="brand-roles" style="top:288px">Magician | <span class="accent">Mentalist</span> | Speaker</div>
    <div class="studio" style="top:318px;font-size:15px">Sleight Lane Productions</div>
    <div class="phone" style="top:338px">505 555 0142</div>
    <ul class="contact-list" style="top:380px">
      <li>
        <svg width="10" height="10" viewBox="0 0 10 10" aria-hidden="true"><circle cx="5" cy="5" r="4" fill="none" stroke="var(--red)" stroke-width="1.2"/><path d="M1 5h8M5 1c-2 2-2 6 0 8M5 1c2 2 2 6 0 8" fill="none" stroke="var(--red)" stroke-width=".8"/></svg>
        <span style="font-family:'Tinos',serif;font-weight:700;font-size:10px">www.walterbrisbymagic.example</span>
      </li>
      <li>
        <svg width="11" height="8" viewBox="0 0 11 8" aria-hidden="true"><rect x=".5" y=".5" width="10" height="7" fill="none" stroke="var(--red)"/><path d="M.5 .5 5.5 4.5 10.5 .5" fill="none" stroke="var(--red)"/></svg>
        <span style="font-size:9.5px">walterbrisbymagic@mailbox.example</span>
      </li>
      <li>
        <span class="square"></span>
        <span style="font-size:9.5px">/Walter-Brisby-Magician-Mentalist</span>
      </li>
    </ul>
  </div>

  <div class="panel panel--c" style="background:linear-gradient(180deg,#000 0%,#000 50%,var(--red-deep) 72%,var(--red) 100%)">
    <div class="photo" role="img" aria-label="Silver light burst radiating behind the name"
      style="left:0;top:0;width:246px;height:200px;background:radial-gradient(ellipse at 50% 40%,#9a9a9a 0%,#4a4a4a 35%,#000 75%)"></div>
    <div class="brand-name" style="top:118px;font-size:19px;color:var(--ink)">walter brisby</div>
    <div class="brand-roles" style="top:144px;color:var(--ink)">Magician | <span class="accent">Mentalist</span> | Speaker</div>
    <div class="photo" role="img" aria-label="Photo of the magician performing a rope trick with a woman in a black dress"
      style="left:0;top:180px;width:246px;height:240px;background:linear-gradient(160deg,#1c223d,#30304a 50%,#4a2025);clip-path:polygon(0 40px,160px 18px,246px 32px,246px 200px,140px 230px,0 210px)"></div>
    <svg class="deco" width="246" height="430" viewBox="0 0 246 430" aria-hidden="true">
      <polyline points="0,216 140,236 246,206" fill="none" stroke="var(--silver)" stroke-width="3"/>
      <polyline points="0,224 140,244 246,214" fill="none" stroke="var(--red-bright)" stroke-width="6"/>
    </svg>
    <div class="pill pill--tagline" style="top:448px">ELEVATE YOUR EVENT WITH MAGIC</div>
    <div class="site-line" style="top:480px">www.walterbrisbymagic.example</div>
    <div class="studio" style="top:493px;font-size:17px;color:var(--black)">Sleight Lane Productions</div>
  </div>
</section>

<section class="sheet sheet--inside">

  <div class="panel panel--a fill-red-soft"></div>
  <div class="panel panel--b" style="background:var(--black)"></div>

  <div class="photo" role="img" aria-label="Photo of the magician performing for a seated corporate audience at banquet tables"
    style="left:0;top:0;width:496px;height:190px;background:linear-gradient(170deg,#7b6a55,#5a4a3c 45%,#3a2f2a);clip-path:polygon(0 0,496px 0,496px 80px,250px 180px,0 130px)"></div>
  <svg class="deco" width="496" height="210" viewBox="0 0 496 210" aria-hidden="true">
    <polyline points="0,132 250,182 496,82" fill="none" stroke="var(--white)" stroke-width="3"/>
    <polyline points="0,140 250,190 496,90" fill="none" stroke="var(--red-bright)" stroke-width="7"/>
  </svg>

  <div class="pill pill--keynote" style="left:126px;top:200px">KEYNOTE SPEAKER</div>
  <div class="body-copy body-copy--tight" style="left:18px;top:229px;width:222px">
    <p>Your audience will be captivated with Walter’s engaging &amp; informative insights on many topics mastered with over 30 years in sales, sales training, and sales management using his “Magic Formula” to personalize his presentation to fit your needs. stage show in st louis shirt 001Walter presents key content with magic, humor &amp; audience participation so that you “learn while you laugh”! Walter combines the power of Magic &amp; Message, using tried &amp; tested techniques &amp; tools to ensure the audience remembers the message.</p>
    <p style="margin-top:0">For years, Walter has presented customized performances for team-building events, keynote speaking, marketing presentations, entrepreneurial training &amp; sales events. Walter’s strength lies is being able to understand your company’s event goals &amp; to deliver them so that the audience ‘locks in’ &amp; remembers the key points. Walter has 30 plus years of experience in the hospitality industry in sales, marketing, training, business development, and Sr. Management working for the leaders in this industry that give him knowledge and experience most magicians, or other speakers cannot offer.</p>
  </div>
  <div class="photo" role="img" aria-label="Photo of the magician performing outdoors beside his show sign"
    style="left:0;top:462px;width:252px;height:66px;background:linear-gradient(180deg,#6f8a6a,#4d5f44);clip-path:polygon(0 14px,252px 0,252px 66px,0 66px)"></div>
  <svg class="deco" width="252" height="528" viewBox="0 0 252 528" aria-hidden="true">
    <polyline points="0,476 252,462" fill="none" stroke="var(--silver)" stroke-width="3"/>
  </svg>

  <div class="pill pill--services" style="left:374px;top:196px">SERVICES</div>
  <p class="body-copy" style="left:264px;top:238px;width:218px;text-align:left">Walter entertains and presents key content with magic, humor and audience participation so that you learn while you laugh!</p>
  <ul class="service-list" style="left:264px;top:284px">
    <li>Corporate Magic</li><li>Sales Training</li><li>Trade Shows</li>
  </ul>
  <ul class="service-list" style="left:392px;top:284px">
    <li>Keynote Speaker</li><li>Magic Shows</li>
  </ul>
  <div class="photo" role="img" aria-label="Photo of the magician performing close-up magic for a smiling woman"
    style="left:252px;top:348px;width:244px;height:180px;background:linear-gradient(180deg,#4a3a33,#2b2422 60%,#1a1a1a);clip-path:polygon(0 30px,122px 0,244px 30px,244px 180px,0 180px)"></div>

  <div class="panel panel--c fill-red-soft">
    <div class="eyebrow" style="top:14px">MY PERFORMANCES ARE</div>
    <div class="headline" style="top:30px;font-size:21px;font-weight:700">GUARANTEED!</div>
    <p class="body-copy body-copy--tight" style="left:11px;top:64px;width:226px">I pride myself on building relationships with my customers, so I’m not happy unless you’re happy. I guarantee your guests will have a great time and will thank you for having me there. If you aren’t thrilled with my performance, just let me know and I’ll refund your money. The only reason I’m able to offer such a guarantee is because I’m very confident you will love doing business with me. In four decades of performing, I’ve never had anyone ask for their money back, and many of my clients hire me again and again.</p>
    <div class="eyebrow" style="top:168px">DOING BUSINESS WITH ME</div>
    <div class="headline" style="top:184px;font-size:26px">IS EASY</div>
    <p class="body-copy body-copy--tight" style="left:11px;top:218px;width:226px">I make sure you’re comfortable with every step in the process of dealing with me. From booking to follow-up you’ll be happy. I arrive early to your event, start on time, and deliver a great performance. You might have a lot on your mind on the day of your event, but worrying about the entertainment won’t be one of them.</p>
    <div class="headline" style="top:292px;font-size:27px">I WORK CLEAN</div>
    <p class="body-copy body-copy--tight" style="left:11px;top:332px;width:226px">Yes, not only do I bathe every day, but all of my comedy is corporate clean. You won’t hear any blue material in my show, and I won’t embarrass anyone. You can rest assured that all of your guests will be treated with respect and look like stars.</p>
    <div class="photo" role="img" aria-label="Portrait photo of the magician smiling, wearing glasses and a dark suit"
      style="left:0;top:386px;width:246px;height:142px;background:linear-gradient(150deg,var(--red) 0%,var(--red-deep) 40%,#1e2740 75%,#2c3550);clip-path:polygon(0 142px,246px 0,246px 142px)"></div>
    <svg class="deco" width="246" height="528" viewBox="0 0 246 528" aria-hidden="true">
      <polyline points="0,530 246,388" fill="none" stroke="var(--white)" stroke-width="3"/>
    </svg>
  </div>
</section>

</body>
</html>
```